依頼詳細
今回作成するチラシは朝凪新報様へ折込む集客チラシの作成です。
しっかり集客ができる動線で作っていただきたいです。
「集客」という目標が最大限できれば、それ以外は求めません。
ターゲットは50代夫婦で子供は独立している方々です。お金は多少余裕があり、お庭の雑草対策に悩んでいる方へ最新技術の雑草の生えない人工芝をしっかりアピール(集客)したいです。
また、このチラシで集客するために、訪問見積もりご依頼いただいたお客様対象「限定15名 スパークリングワイン&スペシャルグラスプレゼント」キャンペーンをする予定です。
スパークリングワイン1本とスペシャルグラス2つプレゼントです。URLは以下の通りです。

https://www.kaimono-ichiba.example/[ルミオン]Lumion-フルートグラス-ステムレスグラスセット/dp/X00000001/

https://www.kaimono-ichiba.example/コルネット-厳選泡6本セット-750mlx6本ワインセット/dp/X00000002/
記載項目
社名:緑野芝生工房株式会社 / 電話:0120-555-318 / URL:tobu-lawn.example
サイズ
A4
ページ数
片面
希望イメージ
シンプル 複雑
単色 カラフル
暗い 明るい
日常 高級
遊び心 厳粛
未来的 伝統的
女性的 男性的
希望する色
緑系、集客さえできるチラシであれば何色を使っても正解です。
補足説明
必要な画像は弊社ホームページからいくらでも転用ください。
そのほか必要な画像は申しつけください。
追加でイメージをお伝えします。
新聞購読者が弊社折込チラシをパッと見て捨てないデザイン(インパクト・限定感・わかりやすさ)で、
電話番号大きくして「今すぐ電話しよう!」と自然とすぐ行動するような導線にしてください。
データを参考に添付します。
【仕様変更】

依頼内容の大幅な変更をお願いいたします。
キャンペーン「スパークリング ワイン・グラスプレゼント」は中止となりました。
もうすでにお取り組みされておられるランサーの方々には大変申し訳ございませんが、「スパークリングワイン・グラスプレゼント」は記載しないようお願いいたします。
また、その代わりにキャンペーン文言「もうすぐ完売! 【キャンペーンプラン】」というように訴求くださると助かります。(訴求のためでしたら追加で【急げ!】【期間限定!】等を追加で入れても問題ございません。)

「もうすぐ完売! 【キャンペーンプラン】」について補足いたします。
弊社では人工芝工事に「エコノミープラン」「ビジネスプラン」「ファーストクラスプラン」がありますが、
キャンペーンプランは通常の「ビジネスプラン」より約21,000円お安く工事が可能なプランです。
(上記のプランの説明を入れることは必須ということではございません。あくまでランサー様へご理解いただくため記載申し上げました。)
内容が大幅に変更となったこと、重ねてお詫び申し上げます。
■ 選んだ理由

訴求から問い合わせまでの動線と内容がよく、木になる人にも情報を提供していたため、デザインだけでなく、情報提供力に優れていたからです。

■ 提案者全員のお礼・コメント

ご提案くださりました全ての方々に、御礼申し上げます。
次回以降ももし可能でしたら優秀な皆様にまたご提案いただけますと嬉しい限りでございます。

```html
<!DOCTYPE html>
<html lang="ja">
<head>
<meta charset="utf-8">
<title>お庭、青くしませんか。｜緑野芝生工房</title>
<link href="https://fonts.googleapis.com/css2?family=Noto+Sans+JP:wght@400;700;900&family=M+PLUS+Rounded+1c:wght@800&display=swap" rel="stylesheet">
<style>
  :root{
    --red:#e3211c;
    --deep-red:#c4120f;
    --green:#3f8f2a;
    --lawn:#5fa83a;
    --navy:#1d3f8f;
    --blue:#2a62c7;
    --yellow:#ffe14a;
    --orange:#f28a12;
    --gold:#c9a445;
    --ink:#222;
    --paper:#fff;
    --soft:#f3f5ef;
  }
  *{margin:0;padding:0;box-sizing:border-box}
  html,body{width:849px;height:1200px;overflow:hidden;background:var(--paper)}
  body{font-family:"Noto Sans JP",sans-serif;color:var(--ink)}
  .flyer{position:relative;width:849px;height:1200px;overflow:hidden;background:var(--paper)}
  .abs{position:absolute}
  .rounded{font-family:"M PLUS Rounded 1c",sans-serif;font-weight:800}
  .hero-photo{left:0;top:0;width:849px;height:330px;background:linear-gradient(180deg,#cfd8c6 0%,#9ab77f 45%,#5d9a34 100%)}
  .headline{left:20px;top:165px;line-height:1.05;white-space:nowrap;
    text-shadow:0 0 6px #fff,3px 3px 0 #fff,-3px -3px 0 #fff,3px -3px 0 #fff,-3px 3px 0 #fff,0 4px 0 #fff,4px 0 0 #fff}
  .headline .line1{display:block;font-size:64px;color:#3a2a1c}
  .headline .line2{display:block;font-size:92px;color:var(--red);letter-spacing:-2px}
  .pro-band{left:150px;top:336px;width:550px;height:52px;border-radius:26px;background:var(--paper);border:3px solid var(--red);
    display:flex;align-items:center;justify-content:center;font-weight:900;font-size:34px;color:var(--red);white-space:nowrap}
  .pro-band small{font-size:26px;color:var(--ink)}
  .features{left:12px;top:398px;width:825px;height:236px;display:grid;grid-template-columns:repeat(4,1fr);gap:8px}
  .feature{position:relative;border-radius:6px;overflow:hidden}
  .feature .photo{position:absolute;inset:0}
  .f1 .photo{background:linear-gradient(160deg,#b9c7ad,#6f9a4e)}
  .f2 .photo{background:linear-gradient(160deg,#b8a58b,#7c6b55)}
  .f3 .photo{background:linear-gradient(160deg,#7fb458,#3e7a25)}
  .f4 .photo{background:linear-gradient(160deg,#8cc55f,#4f8f2e 60%,#8a6a3c)}
  .feature .label{position:absolute;left:10px;bottom:14px;font-size:29px;color:var(--red);white-space:nowrap;
    text-shadow:2px 2px 0 #fff,-2px -2px 0 #fff,2px -2px 0 #fff,-2px 2px 0 #fff;transform:rotate(-6deg);transform-origin:left bottom}
  .promise{width:112px;height:112px;border-radius:50%;border:3px solid var(--red);background:var(--paper);
    display:flex;align-items:center;justify-content:center;text-align:center;font-weight:900;color:var(--red);font-size:20px;line-height:1.2}
  .promise.free{left:16px;top:645px}
  .promise.guarantee{left:136px;top:645px;font-size:17px;color:var(--ink)}
  .satisfaction{left:260px;top:645px;width:290px;height:120px;border:3px solid var(--red);border-radius:8px;background:var(--paper);text-align:center;padding-top:6px}
  .satisfaction .tag{display:inline-block;background:var(--red);color:#fff;font-weight:900;font-size:22px;padding:2px 14px;border-radius:4px}
  .satisfaction .rate{font-size:58px;color:var(--red);line-height:1}
  .satisfaction .rate span{font-size:32px}
  .satisfaction .note{font-size:10px;color:#555;margin-top:2px}
  .award{left:562px;top:645px;width:275px;height:120px;border-radius:8px;background:linear-gradient(180deg,#e9d593,var(--gold))}
  .price-photo{left:16px;top:770px;width:534px;height:50px;background:linear-gradient(90deg,#7aa95a,#b9d3a0)}
  .price{left:22px;top:774px;font-weight:900;font-size:28px;white-space:nowrap;color:var(--yellow);text-shadow:2px 2px 0 var(--deep-red),-2px -2px 0 var(--deep-red),2px -2px 0 var(--deep-red),-2px 2px 0 var(--deep-red)}
  .price .unit{font-size:22px}
  .price .after{font-size:22px;color:#fff}
  .campaign{left:16px;top:826px;display:flex;align-items:center;gap:10px;white-space:nowrap}
  .campaign .soon{background:var(--blue);color:#fff;font-size:26px;padding:4px 14px;transform:rotate(-4deg);border-radius:4px}
  .campaign .plan{font-size:42px;color:var(--red);text-shadow:2px 2px 0 var(--yellow)}
  .limited{left:718px;top:772px;width:122px;height:122px}
  .offer{left:16px;top:880px;font-weight:900;font-size:24px;color:var(--navy);white-space:nowrap;line-height:1.4}
  .offer .big{font-size:34px;color:var(--red)}
  .notes{left:16px;top:932px;width:817px;font-size:11px;line-height:1.45;color:#333}
  .tel-bar{left:0;top:984px;width:849px;height:84px;background:var(--soft);border-top:4px solid var(--green);border-bottom:4px solid var(--green);
    display:flex;align-items:center;justify-content:center;gap:16px}
  .tel-bar .icon{width:70px;height:50px}
  .tel-bar .number{font-size:68px;color:var(--red);letter-spacing:1px;line-height:1;white-space:nowrap}
  .company{left:16px;top:1080px;width:560px}
  .brand{display:flex;align-items:center;gap:8px;font-weight:900;font-size:26px;color:var(--green)}
  .brand .mark{width:22px;height:22px;background:var(--green);border-radius:50%}
  .company .mail{margin-top:6px;font-weight:700;font-size:19px;color:var(--ink)}
  .company .addr{margin-top:4px;font-size:13px;color:#333}
  .web-box{left:592px;top:1080px;width:241px;height:106px;border:2px solid var(--green);border-radius:6px;padding:8px;font-size:13px;line-height:1.5;font-weight:700;color:var(--green)}
  .web-box .url{margin-top:6px;font-size:14px;color:var(--ink)}
</style>
</head>
<body>
<main class="flyer">
  <div class="abs hero-photo" role="img" aria-label="人工芝の庭で遊ぶ子どもと犬の写真"></div>
  <h1 class="abs headline rounded"><span class="line1">お庭、</span><span class="line2">青くしませんか。</span></h1>
  <div class="abs pro-band">プロの施工<small>は</small>ここが違う！</div>

  <section class="abs features">
    <div class="feature f1"><div class="photo" role="img" aria-label="耐久性の高い人工芝の施工写真"></div><span class="label rounded">耐久の良さ</span></div>
    <div class="feature f2"><div class="photo" role="img" aria-label="下地処理の作業写真"></div><span class="label rounded">下地処理</span></div>
    <div class="feature f3"><div class="photo" role="img" aria-label="高品質な人工芝の接写写真"></div><span class="label rounded">品質の高さ</span></div>
    <div class="feature f4"><div class="photo" role="img" aria-label="色違いの人工芝サンプルの写真"></div><span class="label rounded">豊富なカラー</span></div>
  </section>

  <div class="abs promise free">お見積り<br>無料！</div>
  <div class="abs promise guarantee">不満なら<br>直す保証<br>付</div>
  <div class="abs satisfaction">
    <span class="tag">お客様満足度</span>
    <div class="rate rounded">98<span>%</span></div>
    <div class="note">※当社施工のお客様アンケート集計による</div>
  </div>
  <div class="abs award" role="img" aria-label="人工芝施工部門での受賞を示す表彰バッジ"></div>

  <div class="abs price-photo" role="img" aria-label="施工後の人工芝の庭の写真"></div>
  <div class="abs price">1平米<span class="unit"> 7800円</span><span class="after">から施工できます！</span></div>

  <div class="abs campaign rounded"><span class="soon">もうすぐ完売！</span><span class="plan">キャンペーンプラン！！</span></div>
  <svg class="abs limited" viewBox="0 0 122 122" aria-label="5名様限定">
    <circle cx="61" cy="61" r="58" fill="#e3211c"/>
    <circle cx="61" cy="61" r="50" fill="none" stroke="#fff" stroke-width="2"/>
    <text x="61" y="58" text-anchor="middle" font-family="Noto Sans JP, sans-serif" font-weight="900" font-size="30" fill="#ffe14a">5名様</text>
    <text x="61" y="88" text-anchor="middle" font-family="Noto Sans JP, sans-serif" font-weight="900" font-size="26" fill="#fff">限定</text>
  </svg>

  <p class="abs offer">期間限定で通常の「ビジネスプラン」より約<span class="big">21,000円</span> OFF！！</p>
  <p class="abs notes">※キャンペーンは先着順となり、定員に達し次第終了いたします。お早めにお問い合わせください。<br>※施工面積や下地の状態によって金額が変わる場合がございます。詳しくはお電話でご確認ください。<br>※お見積りは無料です。ご相談だけでもお気軽にどうぞ。</p>

  <div class="abs tel-bar">
    <svg class="icon" viewBox="0 0 70 50" aria-label="電話">
      <rect x="2" y="2" width="66" height="46" rx="8" fill="#3f8f2a"/>
      <path d="M22 14c-3 0-5 3-4 7 2 7 8 13 15 15 4 1 7-1 7-4l-5-4-3 2c-3-1-6-4-7-7l2-3z" fill="#fff"/>
      <text x="50" y="32" text-anchor="middle" font-family="Noto Sans JP, sans-serif" font-weight="900" font-size="14" fill="#fff">無料</text>
    </svg>
    <span class="number rounded">0120-555-318</span>
  </div>

  <div class="abs company">
    <div class="brand"><span class="mark"></span>緑野芝生工房</div>
    <p class="mail">MAIL：info@tobu-lawn.example</p>
    <p class="addr">緑野芝生工房株式会社　住所：埼玉県架空市芝原2-12-8</p>
  </div>
  <div class="abs web-box">詳しくは弊社ホームページをご覧ください。施工事例も多数掲載中です。<p class="url">tobu-lawn.example</p></div>
</main>
</body>
</html>
```